Animal Eye Clinic needs a Business card

We are a new veterinary ophthalmology practice (Tessaly Animal Eye Care) and we need a business card designed. We only see animal eyes - we are not a regular veterinary clinic. We already have a logo. We are looking for a professional, good looking business card to hand out to our clients. We are looking for something simple but professional and contemporary. Our logo is likely the only picture/graphic that needs to be on the card.
Updates

Contact Information for Business Card

Marisol Dunkley, BSc, DVM, MSc, DipACVO
Veterinary Ophthalmologist

Phone: 250.418.3097
Email: tessalyanimaleyecare@mailbrook.net
Website: tessalyanimaleyecare.net
Address: 1840 Pellworth Rd
Kelowna, BC, V4T 8M3

Colors

Designer to choose colors to be used in the design.

Requirements
Must have
• Our logo (attached)

```html
<!DOCTYPE html>
<html lang="en">
<head>
<meta charset="utf-8">
<title>Tessaly Animal Eye Care – Business Card</title>
<link href="https://fonts.googleapis.com/css2?family=Raleway:wght@400;500&family=Poppins:wght@300&display=swap" rel="stylesheet">
<style>
  :root {
    --teal: #0893a6;
    --bar-gray: #6f6f6f;
    --text-gray: #6a6a6a;
    --mark-gray: #dadada;
    --card-white: #ffffff;
    --backdrop: #eceff0;
    --on-teal: #ffffff;
  }
  html, body {
    margin: 0;
    padding: 0;
    width: 1200px;
    height: 1200px;
    overflow: hidden;
    background: var(--backdrop);
  }
  .canvas {
    position: relative;
    width: 1200px;
    height: 1200px;
  }
  .card {
    position: absolute;
    left: 174px;
    width: 852px;
    height: 486px;
    overflow: hidden;
    box-shadow: 0 2px 10px rgba(0,0,0,0.08);
  }
  /* Front */
  .card-front {
    top: 79px;
    background: var(--teal);
    display: flex;
    align-items: center;
    justify-content: center;
  }
  .brand {
    display: flex;
    align-items: center;
    gap: 24px;
  }
  .brand-dot {
    width: 72px;
    height: 72px;
    border-radius: 50%;
    background: var(--on-teal);
    flex: none;
  }
  .brand-name {
    margin: 0;
    font-family: "Raleway", sans-serif;
    font-weight: 500;
    color: var(--on-teal);
    font-size: 38px;
    line-height: 1;
    letter-spacing: 0.5px;
    white-space: nowrap;
  }
  /* Back */
  .card-back {
    top: 635px;
    background: var(--card-white);
  }
  .side-bar {
    position: absolute;
    left: 0;
    top: 0;
    width: 15px;
    height: 100%;
  }
  .side-bar .bar-top { height: 242px; background: var(--teal); }
  .side-bar .bar-bottom { height: 244px; background: var(--bar-gray); }
  .back-mark {
    position: absolute;
    left: 576px;
    top: 103px;
    width: 276px;
    height: 276px;
  }
  .person {
    position: absolute;
    left: 64px;
    top: 72px;
  }
  .person-name {
    margin: 0;
    font-family: "Raleway", sans-serif;
    font-weight: 500;
    font-size: 40px;
    line-height: 1;
    color: var(--teal);
  }
  .person-degrees {
    margin: 2px 0 0;
    font-family: "Raleway", sans-serif;
    font-weight: 400;
    font-size: 21px;
    color: var(--teal);
    letter-spacing: 0.3px;
  }
  .person-role {
    margin: 12px 0 0 2px;
    font-family: "Raleway", sans-serif;
    font-weight: 500;
    font-size: 16px;
    color: var(--teal);
    letter-spacing: 1.3px;
  }
  .contacts {
    position: absolute;
    left: 64px;
    top: 324px;
    margin: 0;
    padding: 0;
    list-style: none;
    font-family: "Poppins", sans-serif;
    font-weight: 300;
    font-size: 15px;
    line-height: 20.5px;
    letter-spacing: 1.2px;
    color: var(--text-gray);
  }
  .contacts .label {
    display: inline-block;
    width: 22px;
  }
</style>
</head>
<body>
<main class="canvas">
  <section class="card card-front" aria-label="Card front">
    <div class="brand">
      <div class="brand-dot"></div>
      <h1 class="brand-name">Tessaly Animal Eye Care</h1>
    </div>
  </section>

  <section class="card card-back" aria-label="Card back">
    <div class="side-bar"><div class="bar-top"></div><div class="bar-bottom"></div></div>
    <svg class="back-mark" viewBox="0 0 276 276" aria-hidden="true">
      <circle cx="138" cy="138" r="138" fill="var(--mark-gray)"/>
    </svg>
    <div class="person">
      <h2 class="person-name">Marisol Dunkley</h2>
      <p class="person-degrees">BSc, DVM, MSc, DipACVO</p>
      <p class="person-role">Veterinary Ophthalmologist</p>
    </div>
    <ul class="contacts">
      <li><span class="label">P</span>: 250.418.3097</li>
      <li><span class="label">W</span>: tessalyanimaleyecare.net</li>
      <li><span class="label">E</span>: tessalyanimaleyecare@mailbrook.net</li>
      <li><span class="label">A</span>: 1840 Pellworth Rd, Kelowna, BC, V4T 8M3.</li>
    </ul>
  </section>
</main>
</body>
</html>
```